Baby prediction and advice cards, thank you notes, Baby shower invitations and diaper raffle tickets

Please see attached brief with description of the project.

*** Only apply if you are DETAIL ORIENTED and willing to read 100% the brief and the correction instructions (if required)***

*** Only apply if you are able to communicate in English 100%***

We need QUALITY over quantity

Contact us if you have questions.

Thank you

Target Market(s)

Expecting mothers and their families (Mothers, sisters)

Font styles to use
Sans Serif

Colors

Designer to choose colors to be used in the design.

Requirements
Must have
• Read the brief
Should not have
• Read the brief

```html
<!DOCTYPE html>
<html lang="en">
<head>
<meta charset="utf-8">
<title>Baby Shower Invitation and Diaper Raffle Ticket</title>
<link rel="stylesheet" href="https://fonts.googleapis.com/css2?family=Didact+Gothic&family=Open+Sans:wght@400&family=Patrick+Hand&display=swap">
<style>
  :root {
    --kraft: #b8855f;
    --kraft-light: #d6a480;
    --kraft-band: #c79b79;
    --paper: #ffffff;
    --cream: #f8f0ea;
    --ink: #a87752;
    --ink-soft: #c4a084;
    --label: #8e6446;
    --pink: #f3b0cb;
    --lavender: #dcdaf0;
  }
  html, body {
    margin: 0;
    padding: 0;
    width: 1200px;
    height: 960px;
    overflow: hidden;
    background: var(--paper);
  }
  .canvas {
    position: relative;
    width: 1200px;
    height: 960px;
  }
  .invitation {
    position: absolute;
    left: 44px;
    top: 46px;
    width: 596px;
    height: 842px;
    background: var(--kraft);
    overflow: hidden;
  }
  .invitation__band {
    position: absolute;
    left: 0;
    bottom: 0;
    width: 100%;
    height: 256px;
    background: var(--kraft-band);
  }
  .invitation__art {
    position: absolute;
    inset: 0;
  }
  .invitation__headline {
    position: absolute;
    left: 0;
    top: 146px;
    width: 596px;
    margin: 0;
    text-align: center;
    font-family: "Didact Gothic", sans-serif;
    font-weight: 400;
    font-size: 64px;
    line-height: 78px;
    color: var(--ink);
  }
  .invitation__lead {
    position: absolute;
    left: 0;
    top: 384px;
    width: 596px;
    margin: 0;
    text-align: center;
    font-family: "Patrick Hand", cursive;
    font-size: 24px;
    letter-spacing: 0.5px;
    color: var(--ink);
  }
  .details {
    position: absolute;
    left: 46px;
    top: 542px;
    width: 504px;
    height: 280px;
    background: var(--paper);
    border-radius: 30px;
    box-shadow: 0 0 0 2px #9b6e4d;
  }
  .details::before {
    content: "";
    position: absolute;
    inset: 7px;
    border: 2px dashed var(--kraft);
    border-radius: 24px;
  }
  .details__list {
    position: absolute;
    left: 28px;
    top: 20px;
    margin: 0;
    padding: 0;
    list-style: none;
    font-family: "Didact Gothic", sans-serif;
    font-size: 21px;
    line-height: 34.8px;
    color: var(--ink);
  }
  .ticket {
    position: absolute;
    left: 706px;
    top: 302px;
    width: 460px;
    height: 264px;
    background: var(--kraft);
  }
  .ticket__art {
    position: absolute;
    inset: 0;
  }
  .ticket__title {
    position: absolute;
    left: 62px;
    top: 38px;
    width: 344px;
    height: 56px;
    margin: 0;
    background: var(--kraft);
    border-radius: 8px;
    text-align: center;
    font-family: "Didact Gothic", sans-serif;
    font-weight: 400;
    font-size: 32px;
    line-height: 56px;
    color: var(--paper);
  }
  .ticket__note {
    position: absolute;
    left: 40px;
    top: 138px;
    width: 380px;
    margin: 0;
    text-align: center;
    font-family: "Patrick Hand", cursive;
    font-size: 19px;
    line-height: 22px;
    letter-spacing: 0.4px;
    color: var(--ink);
  }
  .ticket__name {
    position: absolute;
    left: 70px;
    top: 190px;
    margin: 0;
    font-family: "Didact Gothic", sans-serif;
    font-size: 24px;
    color: var(--ink-soft);
  }
  .caption {
    position: absolute;
    margin: 0;
    font-family: "Open Sans", sans-serif;
    font-weight: 400;
    color: var(--label);
    text-align: center;
  }
  .caption--invitation {
    left: 44px;
    top: 896px;
    width: 596px;
    font-size: 44px;
    line-height: 56px;
  }
  .caption--ticket {
    left: 706px;
    top: 586px;
    width: 460px;
    font-size: 44px;
    line-height: 56px;
  }
</style>
</head>
<body>
<main class="canvas">

  <section class="invitation" aria-label="Baby shower invitation">
    <div class="invitation__band" role="img" aria-label="Chevron pattern band"></div>

    <svg class="invitation__art" width="596" height="842" viewBox="0 0 596 842">
      <defs>
        <linearGradient id="balloon-tone" x1="0" y1="0" x2="0" y2="1">
          <stop offset="0" stop-color="var(--pink)"/>
          <stop offset="1" stop-color="var(--lavender)"/>
        </linearGradient>
      </defs>
      <rect class="balloons balloons--left" x="16" y="14" width="136" height="212" rx="60" fill="url(#balloon-tone)" role="img" aria-label="Cluster of pink and lavender balloons"/>
      <rect class="balloons balloons--right" x="434" y="14" width="136" height="196" rx="60" fill="url(#balloon-tone)" role="img" aria-label="Cluster of pink and lavender balloons"/>

      <path class="plaque__rim" fill="var(--kraft-light)"
        d="M100 90 H148 C160 90 165 30 200 30 H396 C431 30 436 90 448 90 H496 Q520 90 520 114 V426 Q520 450 496 450 H448 C436 450 431 510 396 510 H200 C165 510 160 450 148 450 H100 Q76 450 76 426 V114 Q76 90 100 90 Z"/>
      <path class="plaque__face" fill="var(--paper)"
        d="M110 103 H154 C167 103 172 43 204 43 H392 C424 43 429 103 442 103 H486 Q507 103 507 124 V416 Q507 437 486 437 H442 C429 437 424 497 392 497 H204 C172 497 167 437 154 437 H110 Q89 437 89 416 V124 Q89 103 110 103 Z"/>
      <path class="plaque__stitch" fill="none" stroke="var(--ink)" stroke-width="2.5" stroke-dasharray="9 6"
        d="M118 114 H160 C172 114 176 55 208 55 H388 C420 55 424 114 436 114 H478 Q496 114 496 132 V408 Q496 426 478 426 H436 C424 426 420 485 388 485 H208 C176 485 172 426 160 426 H118 Q100 426 100 408 V132 Q100 114 118 114 Z"/>

      <rect class="ornament ornament--top" x="246" y="74" width="104" height="46" rx="10" fill="var(--kraft)" opacity="0.35" role="img" aria-label="Flourish ornament"/>
      <rect class="ornament ornament--bottom" x="256" y="428" width="86" height="38" rx="10" fill="var(--kraft)" opacity="0.35" role="img" aria-label="Flourish ornament"/>
    </svg>

    <h1 class="invitation__headline">“Celebrating<br>a Baby<br>on the way”</h1>
    <p class="invitation__lead">Join us for a shower honoring:</p>

    <div class="details">
      <ul class="details__list">
        <li>Fields:</li>
        <li>Date:</li>
        <li>Time:</li>
        <li>Place:</li>
        <li>Details:</li>
        <li>RSVP to:</li>
        <li>Hosted by:</li>
      </ul>
    </div>
  </section>
  <p class="caption caption--invitation">Invitation card</p>

  <section class="ticket" aria-label="Diaper raffle ticket">
    <svg class="ticket__art" width="460" height="264" viewBox="0 0 460 264">
      <rect class="ticket__paper" x="18" y="16" width="425" height="232" fill="var(--paper)"/>
      <rect class="ticket__chevron" x="18" y="110" width="425" height="138" fill="var(--cream)" role="img" aria-label="Chevron pattern"/>
      <g class="ticket__notches" fill="var(--kraft)">
        <circle cx="18" cy="44" r="12"/><circle cx="18" cy="88" r="12"/>
        <circle cx="18" cy="132" r="12"/><circle cx="18" cy="176" r="12"/>
        <circle cx="18" cy="220" r="12"/>
        <circle cx="443" cy="44" r="12"/><circle cx="443" cy="88" r="12"/>
        <circle cx="443" cy="132" r="12"/><circle cx="443" cy="176" r="12"/>
        <circle cx="443" cy="220" r="12"/>
      </g>
      <rect class="ticket__stitch" x="42" y="24" width="376" height="216" rx="14" fill="none" stroke="var(--ink)" stroke-width="2" stroke-dasharray="7 5"/>
      <rect class="ticket__icon" x="88" y="102" width="28" height="32" rx="8" fill="var(--kraft)" role="img" aria-label="Rubber duck icon"/>
      <rect class="ticket__icon" x="344" y="100" width="30" height="34" rx="8" fill="var(--kraft)" role="img" aria-label="Rocking horse icon"/>
      <g class="ticket__stars" fill="var(--kraft)">
        <polygon transform="translate(152 118)" points="0,-14 4.1,-4.5 13.3,-4.3 6.6,2.9 8.2,11.3 0,7 -8.2,11.3 -6.6,2.9 -13.3,-4.3 -4.1,-4.5"/>
        <polygon transform="translate(191 118)" points="0,-14 4.1,-4.5 13.3,-4.3 6.6,2.9 8.2,11.3 0,7 -8.2,11.3 -6.6,2.9 -13.3,-4.3 -4.1,-4.5"/>
        <polygon transform="translate(230 118)" points="0,-14 4.1,-4.5 13.3,-4.3 6.6,2.9 8.2,11.3 0,7 -8.2,11.3 -6.6,2.9 -13.3,-4.3 -4.1,-4.5"/>
        <polygon transform="translate(268 118)" points="0,-14 4.1,-4.5 13.3,-4.3 6.6,2.9 8.2,11.3 0,7 -8.2,11.3 -6.6,2.9 -13.3,-4.3 -4.1,-4.5"/>
        <polygon transform="translate(307 118)" points="0,-14 4.1,-4.5 13.3,-4.3 6.6,2.9 8.2,11.3 0,7 -8.2,11.3 -6.6,2.9 -13.3,-4.3 -4.1,-4.5"/>
      </g>
    </svg>
    <h2 class="ticket__title">Diaper raffle ticket</h2>
    <p class="ticket__note">Bring a pack of diapers (any size) for<br>your chance to win a prize!</p>
    <p class="ticket__name">Name:</p>
  </section>
  <p class="caption caption--ticket">Ticket Card</p>

</main>
</body>
</html>
```